Varrow Business Card Design - Professional Flexible and forward thinking. Clean and Easy to follow

Management Consulting Company. I focus on business development and concept and operational review. I need a progressive, simple and professional layout design for the business cards, letterhead and envelops
Professional Flexible and forward thinking. Clean and Easy to follow
Mature Business persons and professionals and Corporations

Target Market(s)

Mature Business persons and professionals and Corporations - Government org.

Industry/Entity Type

Consulting

Contact Information for Business Card

Requirements
Must have
• Marcus Varrow
• President
• Phone - 347.682.1530
• email - Mvarrow@varrowpartners-example.com
• Skype - Marc.varrow
• 2187 Tollbrook Lane
• Suite A
• Ashmere Falls, W.R. 11492
• USA
Nice to have
• www.varrowpartners-example.com
Should not have
• N/A

```html
<!DOCTYPE html>
<html lang="en">
<head>
<meta charset="utf-8">
<title>Varrow Associates Business Cards</title>
<link href="https://fonts.googleapis.com/css2?family=Archivo+Narrow:wght@700&family=Arimo:wght@400;700&display=swap" rel="stylesheet">
<style>
  :root {
    --bg: #8a3a22;
    --yellow: #ffcc00;
    --yellow-light: #fff6b8;
    --yellow-bright: #ffea00;
    --ink: #111111;
    --dark: #262626;
    --white: #ffffff;
    --grey: #cfcfcf;
    --tick: #a89a5a;
  }
  * { margin: 0; padding: 0; box-sizing: border-box; }
  html, body { width: 1200px; height: 1108px; overflow: hidden; }
  body { background: var(--bg); position: relative; font-family: "Arimo", Arial, sans-serif; }

  .card { position: absolute; width: 680px; height: 390px; overflow: hidden; box-shadow: 0 8px 24px rgba(0,0,0,.35); }

  /* Front */
  .card-front {
    left: 70px; top: 70px;
    background: radial-gradient(ellipse 55% 60% at 55% 48%, var(--yellow-light) 0%, #ffe24a 40%, var(--yellow) 100%);
    display: flex; align-items: center; justify-content: center;
  }
  .brand { display: flex; align-items: center; gap: 16px; }
  .brand-square { width: 56px; height: 56px; border-radius: 6px; }
  .brand-name { font-family: "Archivo Narrow", "Arial Narrow", sans-serif; font-weight: 700; font-size: 44px; letter-spacing: .5px; white-space: nowrap; }
  .card-front .brand-square { background: var(--ink); }
  .card-front .brand-name { color: var(--ink); }

  /* Back */
  .card-back {
    left: 450px; top: 620px;
    background: radial-gradient(ellipse 50% 55% at 50% 55%, #444 0%, var(--dark) 70%, #1c1c1c 100%);
    color: var(--white);
  }
  .back-header {
    position: absolute; left: 0; top: 0; width: 100%; height: 104px;
    background: linear-gradient(#222, #2b2b2b);
    display: flex; align-items: center; justify-content: center;
  }
  .back-header::after {
    content: ""; position: absolute; left: 0; bottom: -14px; width: 100%; height: 14px;
    background: linear-gradient(#6a6a6a, #2d2d2d);
  }
  .card-back .brand-square { background: var(--yellow); width: 58px; height: 62px; }
  .card-back .brand-name { color: var(--white); font-size: 46px; }

  .person { position: absolute; left: 38px; top: 140px; }
  .person-name {
    font-family: "Archivo Narrow", "Arial Narrow", sans-serif; font-weight: 700;
    font-size: 28px; color: var(--yellow-bright); padding-bottom: 2px;
    border-bottom: 1px solid var(--grey); display: inline-block;
  }
  .person-title { font-size: 12px; margin-top: 6px; }

  .contacts { position: absolute; left: 38px; top: 238px; list-style: none; font-size: 19px; }
  .contacts li { display: flex; align-items: center; gap: 10px; height: 34px; white-space: nowrap; }
  .contacts svg { width: 20px; height: 20px; flex: none; }

  .address { position: absolute; left: 420px; top: 158px; font-size: 19px; line-height: 26px; font-style: normal; white-space: nowrap; }

  .footer-strip { position: absolute; left: 0; bottom: 18px; width: 100%; height: 28px; display: flex; align-items: stretch; }
  .footer-strip .tick { background: var(--tick); margin-right: 6px; }
  .footer-url {
    flex: 1; margin-left: 8px;
    background: linear-gradient(90deg, #b7a550, var(--yellow-bright) 60%);
    color: var(--ink); font-size: 18px; display: flex; align-items: center; justify-content: flex-end; padding-right: 22px; white-space: nowrap;
  }
</style>
</head>
<body>

<section class="card card-front">
  <div class="brand">
    <span class="brand-square"></span>
    <span class="brand-name">VARROW ASSOCIATES</span>
  </div>
</section>

<section class="card card-back">
  <header class="back-header">
    <div class="brand">
      <span class="brand-square"></span>
      <span class="brand-name">VARROW ASSOCIATES</span>
    </div>
  </header>

  <div class="person">
    <div class="person-name">MARCUS VARROW</div>
    <div class="person-title">President</div>
  </div>

  <ul class="contacts">
    <li>
      <svg viewBox="0 0 20 20"><circle cx="10" cy="10" r="9" fill="none" stroke="#fff" stroke-width="1.5"/><path d="M7 5.5c-1 1-1 3 1 5.5s4 3 5 2l-1.5-1.8-1.3.6c-.8-.5-1.8-1.5-2.3-2.4l.7-1.2z" fill="#fff"/></svg>
      347.682.1530
    </li>
    <li>
      <svg viewBox="0 0 20 20"><rect x="1.5" y="4" width="17" height="12" fill="none" stroke="#fff" stroke-width="1.5"/><path d="M1.5 4l8.5 7 8.5-7M1.5 16l6-6M18.5 16l-6-6" fill="none" stroke="#fff" stroke-width="1.3"/></svg>
      Mvarrow@varrowpartners-example.com
    </li>
    <li>
      <svg viewBox="0 0 20 20"><circle cx="10" cy="10" r="9" fill="#fff"/></svg>
      Marc.varrow
    </li>
  </ul>

  <address class="address">
    2187 Tollbrook Lane<br>
    Suite A<br>
    Ashmere Falls, W.R. 11492<br>
    USA
  </address>

  <div class="footer-strip">
    <span class="tick" style="width:3px;margin-right:4px"></span>
    <span class="tick" style="width:4px;margin-right:5px"></span>
    <span class="tick" style="width:6px"></span>
    <span class="tick" style="width:8px"></span>
    <span class="tick" style="width:12px"></span>
    <span class="tick" style="width:16px"></span>
    <span class="tick" style="width:20px"></span>
    <span class="tick" style="width:40px;margin-right:12px"></span>
    <span class="tick" style="width:58px;margin-right:12px"></span>
    <span class="tick" style="width:76px"></span>
    <span class="footer-url">www.varrowpartners-example.com</span>
  </div>
</section>

</body>
</html>
```